"Dario Quillon" Business Card

Friends

My name is "Dario Quillon" and I need your help! I need a new business card for my personal use.

As background, "Dario Quillon" is actually an alias that I use when I meet women. Please use your creative skills to create an amazing business card for me to use!

In addition to including my name and contact details (see the "Must Have" section), you may wish to add a catchphrase or a title if you think it would help me :)

For background, please see:

http://www.dailybrightwire.com/2013/07/23/morton-feld-dario-quillon_n_5129847.html

Looking forward to seeing what you can do for me.

Hugs and kisses,

Dario Quillon [courtesy of PixelHarbor]

Target Market(s)

Adult women in New York City...or anywhere really.

Industry/Entity Type

Business

Requirements
Must have
• Please include the following details:

Dario Quillon
P: +1-555-3QUILLN
E: secrets@darioquillon-mail.com
Nice to have
• You might include a catchphrase, like "Quillon is my surname But you can call me Mr Smoothstep".

Or perhaps a title, like "Dario Quillon, Head of Sexy Times".

You're creative...I will leave the details to you my friends.
Should not have
• Any references to my actual name...because then, what's the point in using an alias?

```html
<!DOCTYPE html>
<html lang="en">
<head>
<meta charset="utf-8">
<title>Dario Quillon Business Card</title>
<link rel="stylesheet" href="https://fonts.googleapis.com/css2?family=Michroma&family=Arimo:wght@400&display=swap">
<style>
  :root {
    --page-bg: #e4e4e4;
    --card-black: #0b0b0b;
    --mesh-light: #2a2a2a;
    --mesh-dark: #050505;
    --silver-hi: #ffffff;
    --silver-mid: #bdbdbd;
    --silver-lo: #6e6e6e;
    --bar-bg: rgba(0, 0, 0, 0.78);
    --text-light: #f2f2f2;
    --tagline: #b8b8b8;
  }
  * { box-sizing: border-box; margin: 0; padding: 0; }
  html, body {
    width: 1200px; height: 861px; overflow: hidden;
    background: var(--page-bg);
  }
  .sheet { position: relative; width: 1200px; height: 861px; }

  .card {
    position: absolute;
    width: 560px; height: 320px;
    background: var(--card-black);
    border-radius: 3px;
    overflow: hidden;
    box-shadow: 0 10px 24px rgba(0,0,0,0.25);
  }
  .card--back  { left: 60px;  top: 60px; }
  .card--front { left: 580px; top: 480px; }

  .card__mesh {
    position: absolute; inset: 0;
    background:
      radial-gradient(ellipse at 70% 20%, rgba(255,255,255,0.10), transparent 55%),
      linear-gradient(160deg, var(--mesh-light), var(--mesh-dark) 70%);
  }

  .card__content { position: relative; height: 100%; }

  /* back side */
  .tagline {
    position: absolute; left: 0; right: 0; top: 90px;
    text-align: center;
    font-family: "Michroma", sans-serif;
    font-variant: small-caps;
    font-size: 26px; line-height: 44px;
    color: var(--tagline);
    letter-spacing: 1px;
  }

  /* front side */
  .name {
    position: absolute; left: 40px; top: 36px;
    font-family: "Michroma", sans-serif;
    font-variant: small-caps;
    font-size: 54px; line-height: 58px;
    background: linear-gradient(180deg, var(--silver-hi) 0%, var(--silver-mid) 45%, var(--silver-lo) 55%, var(--silver-hi) 100%);
    -webkit-background-clip: text; background-clip: text;
    color: transparent;
  }
  .name__line { display: block; }
  .name__line--second { padding-left: 120px; }

  .contacts {
    position: absolute; left: 40px; right: 40px; top: 190px;
    display: flex; flex-direction: column; gap: 12px;
  }
  .contact-bar {
    display: flex; align-items: center; justify-content: space-between;
    height: 42px; padding: 0 14px;
    background: var(--bar-bg);
    font-family: "Arimo", sans-serif;
    font-size: 22px; color: var(--text-light);
    letter-spacing: 0.5px;
  }
  .contact-bar__icon { width: 22px; height: 22px; fill: var(--text-light); flex: none; }
</style>
</head>
<body>
<main class="sheet">

  <section class="card card--back" aria-label="Card back">
    <div class="card__mesh" role="img" aria-label="Dark metal honeycomb mesh texture"></div>
    <div class="card__content">
      <p class="tagline">Quillon is my surname<br>But you can call me<br>Mr. Smoothstep</p>
    </div>
  </section>

  <section class="card card--front" aria-label="Card front">
    <div class="card__mesh" role="img" aria-label="Dark metal honeycomb mesh texture"></div>
    <div class="card__content">
      <h1 class="name">
        <span class="name__line">Dario</span>
        <span class="name__line name__line--second">Quillon</span>
      </h1>
      <div class="contacts">
        <div class="contact-bar">
          <svg class="contact-bar__icon" viewBox="0 0 24 24" aria-hidden="true"><path d="M6.6 10.8a15 15 0 0 0 6.6 6.6l2.2-2.2a1 1 0 0 1 1-.25 11.4 11.4 0 0 0 3.6.6 1 1 0 0 1 1 1V20a1 1 0 0 1-1 1A17 17 0 0 1 3 4a1 1 0 0 1 1-1h3.5a1 1 0 0 1 1 1c0 1.25.2 2.45.6 3.6a1 1 0 0 1-.25 1z"/></svg>
          <span class="contact-bar__text">+1-555-3QUILLN</span>
          <svg class="contact-bar__icon" viewBox="0 0 24 24" aria-hidden="true"><path d="M6.6 10.8a15 15 0 0 0 6.6 6.6l2.2-2.2a1 1 0 0 1 1-.25 11.4 11.4 0 0 0 3.6.6 1 1 0 0 1 1 1V20a1 1 0 0 1-1 1A17 17 0 0 1 3 4a1 1 0 0 1 1-1h3.5a1 1 0 0 1 1 1c0 1.25.2 2.45.6 3.6a1 1 0 0 1-.25 1z"/></svg>
        </div>
        <div class="contact-bar">
          <svg class="contact-bar__icon" viewBox="0 0 24 24" aria-hidden="true"><path d="M2 5h20v14H2z M3.5 6.5 12 13l8.5-6.5" fill="none" stroke="#f2f2f2" stroke-width="1.6"/></svg>
          <span class="contact-bar__text">secrets@darioquillon-mail.com</span>
          <svg class="contact-bar__icon" viewBox="0 0 24 24" aria-hidden="true"><path d="M2 5h20v14H2z M3.5 6.5 12 13l8.5-6.5" fill="none" stroke="#f2f2f2" stroke-width="1.6"/></svg>
        </div>
      </div>
    </div>
  </section>

</main>
</body>
</html>
```